Upscale business cards needed for family office

We would like professional business cards created for employees of our family office. Relatively simple and straightforward, but also with a unique element to set them apart. Probably stick with neutral and simple colors that mesh well with the colors in the logo. We need space for the traditional elements, including name, title, address, email/phone number.

Industry/Entity Type

Business

Contact Information for Business Card

Space for name, title, phone number, email, address

```html
<!DOCTYPE html>
<html lang="en">
<head>
<meta charset="utf-8">
<title>Harrow &amp; Vale — Business Card</title>
<link rel="stylesheet" href="https://fonts.googleapis.com/css2?family=Open+Sans:wght@400;600&display=swap">
<style>
  :root {
    --backdrop: #3b3b3b;
    --card-white: #ffffff;
    --brand-blue: #0894c8;
    --name-blue: #1a8fc4;
    --title-blue: #3f6fb5;
    --ink: #444a50;
    --mark-grey: #5d6670;
    --rule: #c9ccd0;
  }
  * { box-sizing: border-box; margin: 0; padding: 0; }
  html, body {
    width: 1105px; height: 1200px; overflow: hidden;
    background: var(--backdrop);
    font-family: "Open Sans", Arial, sans-serif;
  }
  .card {
    position: absolute; left: 196px;
    width: 720px; height: 411px;
  }
  .card--front { top: 146px; background: var(--card-white); }
  .card--back { top: 602px; background: var(--brand-blue); }

  .brand-mark {
    position: absolute; display: flex; align-items: center; gap: 12px;
    font-weight: 600; white-space: nowrap;
  }
  .brand-mark__square { display: block; width: 18px; height: 18px; flex: none; }
  .card--front .brand-mark {
    left: 70px; top: 102px; width: 250px; height: 202px;
    justify-content: center; font-size: 28px; color: var(--mark-grey);
  }
  .card--front .brand-mark__square { background: var(--brand-blue); }

  .divider {
    position: absolute; left: 341px; top: 88px;
    width: 1px; height: 235px; background: var(--rule);
  }
  .contact { position: absolute; left: 381px; top: 98px; }
  .contact__name {
    font-size: 25px; font-weight: 600; color: var(--name-blue);
    letter-spacing: 0.3px; line-height: 34px;
  }
  .contact__title { font-size: 19px; color: var(--title-blue); line-height: 26px; margin-bottom: 14px; }
  .contact__address { font-size: 19px; color: var(--ink); line-height: 26px; margin-bottom: 6px; }
  .contact__line {
    display: flex; align-items: center; gap: 10px;
    font-size: 19px; color: var(--ink); line-height: 27.5px;
  }
  .contact__line svg { width: 17px; height: 17px; flex: none; }

  .card--back .brand-mark {
    left: 0; right: 0; top: 160px; justify-content: center;
    font-size: 44px; color: #fff;
  }
  .card--back .brand-mark__square { width: 26px; height: 26px; background: #fff; }
  .back-url {
    position: absolute; left: 0; right: 0; top: 340px;
    text-align: center; color: #fff; font-size: 19px; letter-spacing: 5.5px;
  }
</style>
</head>
<body>
  <section class="card card--front">
    <div class="brand-mark"><span class="brand-mark__square"></span>Harrow &amp; Vale</div>
    <div class="divider"></div>
    <div class="contact">
      <p class="contact__name">CLARA VOSS</p>
      <p class="contact__title">CEO/Founder</p>
      <p class="contact__address">214 Harbor View Road<br>Juneau, Alaska 99801</p>
      <p class="contact__line">
        <svg viewBox="0 0 16 16" aria-hidden="true"><path fill="#0894c8" d="M3.6 1.2l2.3 2.6-1.3 1.8c.8 2 2.6 3.8 4.6 4.6l1.8-1.3 2.6 2.3-1.4 2.2C7 13.7 2.3 9 1.6 3l2-1.8z"/></svg>
        907 555 0142
      </p>
      <p class="contact__line">
        <svg viewBox="0 0 16 16" aria-hidden="true"><rect x="1" y="3.5" width="14" height="9.5" fill="#0894c8"/><path d="M1.5 4l6.5 5 6.5-5" fill="none" stroke="#fff" stroke-width="1.2"/></svg>
        clara@harrowvale.com
      </p>
      <p class="contact__line">
        <svg viewBox="0 0 16 16" aria-hidden="true"><circle cx="8" cy="8" r="7" fill="#0894c8"/><path d="M1 8h14M8 1c-3 3-3 11 0 14M8 1c3 3 3 11 0 14" fill="none" stroke="#fff" stroke-width="1"/></svg>
        www.harrowvale.com
      </p>
    </div>
  </section>

  <section class="card card--back">
    <div class="brand-mark"><span class="brand-mark__square"></span>Harrow &amp; Vale</div>
    <p class="back-url">www.harrowvale.com</p>
  </section>
</body>
</html>
```